Security and Automation Company based in Texas and needs logo design also

Looking for a new logo design for our company - we are based in Texas and specialize in camera, security and home automation - We do want the main company name(Brightline Guard and Controls of Texas) with our parent company in small letters below (a Veloran Partners, LLC Company) and our License number needs to be included in the design - K74836 - Darker shades of blue preferred

Target Market(s)

We work with everyone from home to large corporate - so clean design would be helpful

Industry/Entity Type

It Company

Contact Information for Business Card

PO Box 4719
Cedar Hollow, Texas 75961
Leave a spot for the phone number and email address

Logo Text

Brightline Guard and Controls of Texas/a Veloran Partners Company/K74836

Font styles to use
Sans Serif

Colors
0255a3

```html
<!DOCTYPE html>
<html lang="en">
<head>
<meta charset="utf-8">
<title>Brightline Guard and Controls of Texas — Business Card</title>
<link rel="stylesheet" href="https://fonts.googleapis.com/css2?family=Open+Sans:wght@300;400;600&display=swap">
<style>
  :root {
    --navy: #1d4f7e;
    --navy-deep: #163e66;
    --navy-light: #2a6293;
    --red: #e3283d;
    --ink: #2b2b2b;
    --muted: #555b63;
    --paper: #ffffff;
    --paper-shade: #f1f2f4;
    --stage: #e7e4df;
  }
  * { box-sizing: border-box; margin: 0; padding: 0; }
  html, body { width: 771px; height: 1200px; overflow: hidden; }
  body {
    background: var(--stage);
    font-family: "Open Sans", Arial, sans-serif;
    display: flex;
    flex-direction: column;
    align-items: center;
    justify-content: center;
    gap: 90px;
  }
  .card {
    position: relative;
    width: 640px;
    height: 366px;
    border-radius: 18px;
    overflow: hidden;
    box-shadow: 0 10px 28px rgba(0,0,0,.18);
  }
  .brand__mark {
    border-radius: 50%;
    background: var(--red);
    flex: none;
  }

  /* Front */
  .card--front {
    background: radial-gradient(ellipse at 30% 40%, var(--navy-light) 0%, var(--navy) 45%, var(--navy-deep) 100%);
    color: var(--paper);
  }
  .front__brand {
    position: absolute;
    left: 90px;
    top: 118px;
    display: flex;
    align-items: center;
    gap: 22px;
  }
  .front__brand .brand__mark { width: 62px; height: 62px; }
  .front__name {
    font-size: 26px;
    font-weight: 400;
    line-height: 1.18;
    letter-spacing: .5px;
    text-transform: uppercase;
    width: 380px;
  }
  .front__parent {
    position: absolute;
    left: 174px;
    top: 222px;
    font-size: 16px;
    font-weight: 300;
    letter-spacing: .4px;
  }
  .front__license {
    position: absolute;
    left: 174px;
    top: 250px;
    font-size: 13px;
    font-weight: 300;
    letter-spacing: 1.5px;
  }

  /* Back */
  .card--back {
    background: linear-gradient(160deg, var(--paper) 0%, var(--paper) 60%, var(--paper-shade) 100%);
    color: var(--ink);
  }
  .back__brand {
    position: absolute;
    left: 200px;
    top: 40px;
    display: flex;
    align-items: center;
    gap: 12px;
  }
  .back__brand .brand__mark { width: 34px; height: 34px; }
  .back__name {
    font-size: 14px;
    font-weight: 600;
    color: var(--navy);
    text-transform: uppercase;
    line-height: 1.25;
    letter-spacing: .3px;
  }
  .back__license {
    position: absolute;
    left: 246px;
    top: 84px;
    font-size: 11px;
    color: var(--muted);
    letter-spacing: 1px;
  }
  .back__website {
    position: absolute;
    right: 40px;
    top: 150px;
    font-size: 14px;
    color: var(--red);
  }
  .person {
    position: absolute;
    left: 0;
    top: 196px;
    display: flex;
    align-items: center;
  }
  .person__bar {
    width: 54px; height: 24px;
    background: var(--red);
  }
  .person__text { margin-left: 14px; }
  .person__name { font-size: 24px; font-weight: 400; line-height: 1.1; }
  .person__title { font-size: 13px; color: var(--navy); }
  .contact {
    position: absolute;
    left: 170px;
    top: 262px;
    list-style: none;
    font-size: 13px;
    color: var(--ink);
  }
  .contact li {
    display: flex;
    align-items: flex-start;
    gap: 10px;
    margin-bottom: 7px;
    line-height: 1.3;
  }
  .contact svg { width: 14px; height: 14px; flex: none; margin-top: 2px; fill: var(--muted); }
</style>
</head>
<body>

  <section class="card card--front">
    <div class="front__brand">
      <span class="brand__mark"></span>
      <p class="front__name">Brightline Guard and<br>Controls of Texas</p>
    </div>
    <p class="front__parent">a Veloran Partners, LLC Company</p>
    <p class="front__license">LIC. K74836</p>
  </section>

  <section class="card card--back">
    <div class="back__brand">
      <span class="brand__mark"></span>
      <p class="back__name">Brightline Guard and<br>Controls of Texas</p>
    </div>
    <p class="back__license">LIC. K74836</p>

    <p class="back__website">yourwebsite.com</p>

    <div class="person">
      <span class="person__bar"></span>
      <div class="person__text">
        <p class="person__name">Your Name</p>
        <p class="person__title">Job Title</p>
      </div>
    </div>

    <ul class="contact">
      <li>
        <svg viewBox="0 0 16 16" aria-hidden="true"><path d="M2 5c0-1.5 1-2.5 6-2.5S14 3.5 14 5v1h-3V5H5v1H2z"/><rect x="3" y="7" width="10" height="7" rx="1.5"/></svg>
        <span>000 000 0000</span>
      </li>
      <li>
        <svg viewBox="0 0 16 16" aria-hidden="true"><path d="M1 3h14v10H1z M1 3l7 6 7-6" stroke="#fff" stroke-width="1"/></svg>
        <span>youremail@xyz.com</span>
      </li>
      <li>
        <svg viewBox="0 0 16 16" aria-hidden="true"><path d="M8 1a5 5 0 0 0-5 5c0 4 5 9 5 9s5-5 5-9a5 5 0 0 0-5-5zm0 7a2 2 0 1 1 0-4 2 2 0 0 1 0 4z"/></svg>
        <span>PO Box 4719<br>Cedar Hollow, Texas 75961</span>
      </li>
    </ul>
  </section>

</body>
</html>
```